IT consulting firm needs brochures for each of our practices

We have a basic draft of a brochure for each of the practices, we offer services as IT consultants and need a better look for each one. We want to use client logos and information on our expertise for each brochure/practice.
Our website has the different areas we serve as reference.

Industry/Entity Type

Consulting

```html
<!DOCTYPE html>
<html lang="en">
<head>
<meta charset="utf-8">
<title>Norvane Financial Practice – Brochure</title>
<link href="https://fonts.googleapis.com/css2?family=Marcellus&family=Open+Sans:wght@400;600;700&family=Arimo:wght@400&display=swap" rel="stylesheet">
<style>
  :root {
    --bg: #e9e6e2;
    --page-left: #ecebee;
    --blue: #18a3d8;
    --blue-deep: #0a6fbe;
    --heading-blue: #1b7fc1;
    --ink: #1c1c1c;
    --ink-soft: #333333;
    --rule: #555555;
    --white: #ffffff;
    --photo-light: #dfe9f1;
    --photo-mid: #a9bfd0;
    --photo-dark: #4a5058;
  }
  * { box-sizing: border-box; margin: 0; padding: 0; }
  html, body { width: 1200px; height: 970px; overflow: hidden; background: var(--bg); }
  .canvas { position: relative; width: 1200px; height: 970px; }
  .spread {
    position: absolute; left: 120px; top: 165px; width: 960px; height: 640px;
    display: flex; box-shadow: 0 10px 30px rgba(0,0,0,.25);
  }
  .page { position: relative; width: 480px; height: 640px; overflow: hidden; }

  /* Inside page */
  .page--inside { background: var(--page-left); font-family: "Open Sans", sans-serif; }
  .header-band { position: absolute; left: 0; top: 0; width: 480px; height: 120px; }
  .brand {
    position: absolute; left: 0; right: 0; text-align: center;
    font-family: "Open Sans", sans-serif; font-weight: 700; color: var(--white);
    letter-spacing: 2px;
  }
  .page--inside .brand { top: 22px; font-size: 46px; }
  .sla-title {
    position: absolute; top: 108px; left: 0; right: 0; text-align: center;
    font-family: "Marcellus", serif; color: var(--heading-blue); font-size: 19px;
  }
  .sla-text {
    position: absolute; top: 136px; left: 50px; right: 40px;
    font-size: 10.5px; line-height: 1.3; color: var(--ink); text-indent: 30px;
  }
  .rule { position: absolute; top: 222px; left: 48px; right: 38px; border-top: 1px solid var(--rule); }
  .photo-frame {
    position: absolute; top: 236px; left: 130px; width: 250px; height: 160px;
    background: var(--white); border: 1px solid #b9b9b9; padding: 6px;
  }
  .photo-frame .photo {
    width: 100%; height: 100%;
    background: linear-gradient(120deg, var(--photo-dark) 0%, #9aa4ad 30%, var(--photo-light) 60%, #c6ccd2 100%);
  }
  .invite {
    position: absolute; top: 420px; left: 40px; right: 30px;
    font-size: 15.5px; line-height: 1.35; color: var(--ink);
  }
  .contact { position: absolute; top: 512px; left: 0; right: 0; text-align: center; font-family: "Arimo", sans-serif; }
  .contact__name { color: var(--heading-blue); font-size: 17px; }
  .contact__phone { margin-top: 12px; font-size: 16px; color: var(--ink); }
  .contact__web { margin-top: 12px; font-size: 15.5px; color: var(--ink); }

  /* Cover page */
  .page--cover { background: var(--blue); }
  .cover-photo {
    position: absolute; inset: 0;
    background: linear-gradient(90deg, #7f8790 0%, #c3cdd6 30%, var(--photo-light) 55%, var(--photo-mid) 80%, #8796a4 100%);
  }
  .cover-art { position: absolute; inset: 0; width: 480px; height: 640px; }
  .cover-title {
    position: absolute; top: 95px; right: 28px; text-align: right;
    font-family: "Marcellus", serif; color: var(--ink-soft);
  }
  .cover-title__name { font-size: 30px; display: block; }
  .cover-title__practice { font-size: 22px; display: block; margin-top: 2px; }
  .page--cover .brand { top: 440px; left: 60px; font-size: 62px; letter-spacing: 4px; }
  .cover-url {
    position: absolute; top: 558px; left: 60px; right: 0; text-align: center;
    font-family: "Arimo", sans-serif; font-size: 20px; color: var(--white);
  }
</style>
</head>
<body>
<div class="canvas">
  <div class="spread">

    <section class="page page--inside">
      <svg class="header-band" viewBox="0 0 480 120" aria-hidden="true">
        <defs>
          <linearGradient id="bandFill" x1="0" x2="1">
            <stop offset="0" stop-color="#0f8fd0"/>
            <stop offset="1" stop-color="#1fb0e0"/>
          </linearGradient>
        </defs>
        <path d="M0,0 H480 V70 Q240,120 0,80 Z" fill="url(#bandFill)"/>
      </svg>
      <div class="brand">NRV</div>
      <h2 class="sla-title">Service Level Agreement and Commitment</h2>
      <p class="sla-text">Once an issue concerning the use of software is reported, Norvane agrees to assign a resource to verify and investigate the issue. In critical issues (High), this resource will be assigned within specific pre-determine business hours and for regular issues (Low and Medium), the resource will be assigned within one business day and provide immediate resolution.</p>
      <div class="rule"></div>
      <div class="photo-frame">
        <div class="photo" role="img" aria-label="Photo of a consultant at a desk talking on the phone beside a computer monitor"></div>
      </div>
      <p class="invite">Are you interested in learning more about what we have to offer you? We are more than happy to provide additional information about our services. For more details or any other questions you have, contact</p>
      <div class="contact">
        <p class="contact__name">Marina Castellano, VP of Sales</p>
        <p class="contact__phone">(555) 210-4837</p>
        <p class="contact__web">marina.castellano@nrv-consult.com | www.nrv-consult.com</p>
      </div>
    </section>

    <section class="page page--cover">
      <div class="cover-photo" role="img" aria-label="Photo of a smiling businessman in a grey suit with arms crossed, colleagues meeting at a table in a bright office behind him"></div>
      <svg class="cover-art" viewBox="0 0 480 640" aria-hidden="true">
        <defs>
          <linearGradient id="coverBlue" x1="0" x2="1" y1="0" y2="1">
            <stop offset="0" stop-color="#1fb0e0"/>
            <stop offset="1" stop-color="#0a6fbe"/>
          </linearGradient>
        </defs>
        <path d="M0,320 Q150,470 480,350 V640 H0 Z" fill="url(#coverBlue)"/>
      </svg>
      <h1 class="cover-title">
        <span class="cover-title__name">Norvane</span>
        <span class="cover-title__practice">Financial Practice</span>
      </h1>
      <div class="brand">NRV</div>
      <p class="cover-url">www.nrv-consult.com</p>
    </section>

  </div>
</div>
</body>
</html>
```